Social Media Graphics - ALL TEXT RK

We are looking for a series of social media graphics for Instagram (standard size 1:1 (1080x1080px) that are ALL TEXT. We want the following quotes below on each graphic; one quote per graphic. AND, In very small letters at the bottom of each graphic, add @RKMarlowLive

The look and feel of these graphics should be complimentary to the color palette attached below; but keep them simple. But the design is up to you; at the end of this document, I provided various samples of all text graphics that I like as examples.

Target Market(s)

women looking to lose weight

Industry/Entity Type

health and wellness

Colors
E54698
E96AAD
F1A4CE
F9D9EA
FCEFF6

Requirements
Must have
• the quotes in the document
Should not have
• no stock photography

```html
<!DOCTYPE html>
<html lang="en">
<head>
<meta charset="utf-8">
<title>RK Social Quote Tiles</title>
<link rel="stylesheet" href="https://fonts.googleapis.com/css2?family=Montserrat:wght@500;800&display=swap">
<style>
  :root {
    --page: #ffffff;
    --tile-center: #ee6fb2;
    --tile-mid: #d3428f;
    --tile-edge: #a0226a;
    --quote: #ffffff;
    --quote-shadow: rgba(70, 0, 40, 0.55);
    --handle: #fce3f0;
  }
  html, body {
    margin: 0;
    padding: 0;
    width: 1200px;
    height: 1188px;
    overflow: hidden;
    background: var(--page);
  }
  .board {
    position: relative;
    width: 1200px;
    height: 1188px;
  }
  .tile {
    position: absolute;
    background: radial-gradient(circle at 50% 50%, var(--tile-center) 0%, var(--tile-mid) 55%, var(--tile-edge) 100%);
    font-family: "Montserrat", Arial, sans-serif;
    color: var(--quote);
    text-align: center;
  }
  .tile-small { width: 289px; height: 289px; }
  .tile-large { width: 574px; height: 574px; }

  .quote {
    position: absolute;
    left: 0;
    right: 0;
    margin: 0;
    font-weight: 800;
    text-transform: uppercase;
    text-shadow: 2px 2px 2px var(--quote-shadow);
    transform: translateY(-50%);
  }
  .tile-small .quote {
    top: 46%;
    font-size: 18.5px;
    line-height: 22.6px;
    letter-spacing: 0.2px;
  }
  .tile-large .quote {
    top: 48%;
    font-size: 40px;
    line-height: 45px;
    letter-spacing: 0.5px;
  }
  .handle {
    position: absolute;
    left: 0;
    right: 0;
    margin: 0;
    font-weight: 500;
    color: var(--handle);
  }
  .tile-small .handle { bottom: 18px; font-size: 9px; }
  .tile-large .handle { bottom: 38px; font-size: 17px; letter-spacing: 0.3px; }

  .r1 { top: 0; }
  .r2 { top: 304px; }
  .r3 { top: 897px; }
  .c1 { left: 0; }
  .c2 { left: 302px; }
  .c3 { left: 605px; }
  .c4 { left: 908px; }
  .w1 { left: 16px; }
  .w2 { left: 609px; }
</style>
</head>
<body>
<main class="board">
  <section class="tile tile-small r1 c1">
    <p class="quote">Struggling<br>with bloating<br>and belly fat?<br>Try this<br>natural solution<br>tonight, and<br>wake up feeling<br>lighter!</p>
    <p class="handle">@RKMarlowLive</p>
  </section>
  <section class="tile tile-small r1 c2">
    <p class="quote">One supplement,<br>one night;<br>your belly bloat<br>could be gone<br>by morning.<br>Here’s how<br>it works!</p>
    <p class="handle">@RKMarlowLive</p>
  </section>
  <section class="tile tile-small r1 c3">
    <p class="quote">Finally-a<br>natural solution<br>that flattens<br>your belly and<br>eases stomach<br>bloat</p>
    <p class="handle">@RKMarlowLive</p>
  </section>
  <section class="tile tile-small r1 c4">
    <p class="quote">Wake up<br>tomorrow<br>with a flatter<br>belly- yes,<br>this overnight<br>remedy works<br>like magic!</p>
    <p class="handle">@RKMarlowLive</p>
  </section>

  <section class="tile tile-large r2 w1">
    <p class="quote">Sis, your<br>hormones are<br>out of whack -<br>that’s why<br>the weight won’t<br>budge!</p>
    <p class="handle">@RKMarlowLive</p>
  </section>
  <section class="tile tile-large r2 w2">
    <p class="quote">Frustrated<br>with belly fat<br>that won’t budge?<br>I’ve got the<br>solution that<br>finally worked<br>for me-<br>no crazy<br>diets required.</p>
    <p class="handle">@RKMarlowLive</p>
  </section>

  <section class="tile tile-small r3 c1">
    <p class="quote">That stubborn<br>belly fat isn’t<br>your fault - here’s<br>what no one<br>tells you.</p>
    <p class="handle">@RKMarlowLive</p>
  </section>
  <section class="tile tile-small r3 c2">
    <p class="quote">You’ve been<br>lied to - ’just<br>eat less and<br>exercise more’<br>doesn’t work in<br>menopause</p>
    <p class="handle">@RKMarlowLive</p>
  </section>
  <section class="tile tile-small r3 c3">
    <p class="quote">A natural way<br>to boost GLP-1 -<br>no injections,<br>no side effects,<br>just real results.<br>Here’s how<br>it works</p>
    <p class="handle">@RKMarlowLive</p>
  </section>
  <section class="tile tile-small r3 c4">
    <p class="quote">GLP-1:<br>the magic<br>behind the weight<br>loss drugs. But<br>here’s the secret -<br>you can boost<br>it naturally<br>without a<br>prescription!</p>
    <p class="handle">@RKMarlowLive</p>
  </section>
</main>
</body>
</html>
```